Software allocation system needs a business card design

We need a business card designed for our software platform - www.tolvexa.com.au

At the moment the logo and website is all black and white, we are happy for suggestions on implementing some colour throughout either the logo or business card.

Industry/Entity Type

Software

Font styles to use
Sans Serif

Colors

Designer to choose colors to be used in the design.

```html
<!DOCTYPE html>
<html lang="en">
<head>
<meta charset="utf-8">
<title>Tolvexa Business Card</title>
<link rel="stylesheet" href="https://fonts.googleapis.com/css2?family=Roboto:wght@300;400&display=swap">
<style>
  :root {
    --backdrop: #e9e7e3;
    --card-dark: #1d1d1d;
    --card-light: #e4e4e4;
    --ink-dark: #222222;
    --ink-light: #f2f2f2;
    --accent: #d8a21b;
    --shadow: rgba(0, 0, 0, 0.18);
  }
  * { margin: 0; padding: 0; box-sizing: border-box; }
  html, body {
    width: 1200px;
    height: 900px;
    overflow: hidden;
    background: var(--backdrop);
    font-family: "Roboto", Arial, sans-serif;
  }
  .canvas {
    position: relative;
    width: 1200px;
    height: 900px;
  }
  .card {
    position: absolute;
    left: 320px;
    width: 560px;
    height: 320px;
    box-shadow: 0 8px 24px var(--shadow);
  }
  .card--back {
    top: 110px;
    background: var(--card-dark);
  }
  .card--front {
    top: 470px;
    background: var(--card-light);
    color: var(--ink-dark);
  }
  .wordmark {
    font-weight: 300;
    text-transform: uppercase;
    letter-spacing: 0.12em;
    line-height: 1;
  }
  .card--back .wordmark {
    position: absolute;
    left: 0;
    right: 0;
    top: 118px;
    text-align: center;
    font-size: 46px;
    color: var(--ink-light);
  }
  .card--back .web {
    position: absolute;
    left: 0;
    right: 0;
    top: 210px;
    text-align: center;
    font-size: 14px;
    color: var(--accent);
  }
  .card--front .wordmark {
    position: absolute;
    left: 44px;
    top: 52px;
    font-size: 46px;
    color: var(--ink-dark);
  }
  .person {
    position: absolute;
    left: 96px;
    top: 142px;
    font-size: 22px;
    font-weight: 300;
    text-transform: uppercase;
  }
  .person .role {
    font-size: 13px;
    letter-spacing: 0.02em;
  }
  .marker {
    position: absolute;
    left: 52px;
    top: 188px;
  }
  .contact {
    position: absolute;
    left: 52px;
    top: 214px;
    display: grid;
    grid-template-columns: 64px auto;
    row-gap: 2px;
    font-size: 16px;
    font-weight: 300;
    line-height: 1.15;
  }
  .contact dt {
    color: var(--accent);
    text-transform: uppercase;
  }
  .contact dd { color: var(--ink-dark); }
  .address {
    position: absolute;
    right: 40px;
    top: 142px;
    font-size: 14px;
    font-weight: 300;
    font-style: normal;
    line-height: 1.3;
    text-align: left;
  }
  .address .web { color: var(--accent); }
</style>
</head>
<body>
<main class="canvas">
  <section class="card card--back" aria-label="Business card back">
    <div class="wordmark">Tolvexa</div>
    <div class="web">www.tolvexa.com.au</div>
  </section>

  <section class="card card--front" aria-label="Business card front">
    <div class="wordmark">Tolvexa</div>
    <div class="person">Dana Whitford <span class="role">| Manager</span></div>
    <svg class="marker" width="24" height="20" viewBox="0 0 24 20" aria-hidden="true">
      <polygon points="0,0 24,0 12,20" fill="var(--accent)"/>
    </svg>
    <dl class="contact">
      <dt>Phone</dt><dd>214.555.0172</dd>
      <dt>Fax</dt><dd>214.555.0189</dd>
      <dt>Email</dt><dd>dwhitford@tolvexa.com.au</dd>
    </dl>
    <address class="address">
      PO Box 512<br>
      Harlow Bay NSW 2601<br>
      <span class="web">www.tolvexa.com.au</span>
    </address>
  </section>
</main>
</body>
</html>
```